Dietitian needs awesome business card

I need a contemporary design that's eye catching but professional.
My card is to given to doctors, specialists and patients alike.
I manage patients with chronic diseases
I have uploaded my logo and current business card, I would also like the other Registered Clinical Nutritionist logo incorporated into the design

Target Market(s)

Doctors, specialists and patients

Industry/Entity Type

Healthcare

Contact Information for Business Card

www.brindlecovenutrition.com.au
Ph: 0427 516 903
Fax: 6482 7315
email: marcus.k.wellfare@quorvamail.com
Space on the back of the card with: Appointment date, Appointment time and appointment location

Font styles to use
Serif

Colors
fbee3e
876aae
ffc214

Requirements
Must have
• My Logo
• Registered Clinical Nutritionist Logo
• My 4 locations - Fernhollow Medical Centre, North Kelby Health, Ashcourt Medical, Pinebrook Doctors Surgery
Nice to have
• I like the colours in my current business card

```html
<!DOCTYPE html>
<html lang="en">
<head>
<meta charset="utf-8">
<title>Brindle Cove Nutrition &amp; Dietetics – Business Card</title>
<link rel="stylesheet" href="https://fonts.googleapis.com/css2?family=Lato:wght@300;400&display=swap">
<style>
  :root {
    --bg: #e9e6e1;
    --card: #ffffff;
    --green: #66bb3f;
    --green-text: #6cbf3a;
    --blue: #2a4f9c;
    --orange: #f47c20;
    --grey-text: #6b6b6b;
    --rule: #b9b9b9;
    --icon: #4a4a4a;
  }
  * { margin: 0; padding: 0; box-sizing: border-box; }
  html, body { width: 1200px; height: 1023px; overflow: hidden; background: var(--bg); }
  body { position: relative; font-family: "Lato", sans-serif; }

  .card {
    position: absolute; left: 220px;
    width: 760px; height: 434px;
    background: var(--card);
    box-shadow: 0 8px 24px rgba(0,0,0,.16);
    overflow: hidden;
  }
  .card-front { top: 50px; }
  .card-back { top: 540px; }

  /* front */
  .holder-name {
    position: absolute; left: 220px; top: 40px;
    font-weight: 400; font-size: 36px; letter-spacing: 1px;
    color: var(--green-text);
  }
  .contact-list {
    position: absolute; left: 220px; top: 100px;
    list-style: none;
  }
  .contact-list li {
    display: flex; align-items: center; gap: 14px;
    height: 32px;
    font-weight: 300; font-size: 20px; color: var(--grey-text);
  }
  .contact-list svg { width: 22px; height: 22px; flex: none; fill: var(--icon); }

  .brand {
    position: absolute; left: 34px; top: 250px;
    display: flex; align-items: center; gap: 18px;
  }
  .brand-dot {
    width: 86px; height: 86px; border-radius: 50%;
    background: var(--blue); flex: none;
  }
  .brand-name {
    font-weight: 400; font-size: 33px; line-height: 1.05;
    color: var(--blue);
  }

  .band {
    position: absolute; left: 0; bottom: 0;
    width: 100%; height: 84px;
    background: var(--green);
  }
  .credential {
    position: absolute; right: 30px; bottom: 84px;
    width: 160px; height: 110px;
    background: var(--orange);
    display: flex; align-items: center; justify-content: space-between;
    padding: 12px 14px;
  }
  .credential-text {
    font-weight: 400; font-size: 15px; line-height: 1.2; color: #fff;
  }
  .credential-badge {
    width: 48px; height: 48px; border-radius: 50%;
    background: #fff; flex: none; align-self: flex-start;
  }

  /* back */
  .appointment-title {
    position: absolute; left: 60px; top: 50px;
    font-weight: 400; font-size: 34px; letter-spacing: 1px;
    color: var(--grey-text);
  }
  .appointment-fields {
    position: absolute; left: 60px; right: 60px; top: 150px;
    list-style: none;
  }
  .appointment-fields li {
    display: flex; align-items: flex-end; gap: 16px;
    height: 72px;
    font-weight: 300; font-size: 20px; color: var(--grey-text);
  }
  .appointment-fields .label { width: 90px; flex: none; }
  .appointment-fields .line {
    flex: 1; border-bottom: 2px solid var(--rule); margin-bottom: 5px;
  }
</style>
</head>
<body>
  <section class="card card-front">
    <h1 class="holder-name">Marcus Kellaway</h1>

    <ul class="contact-list">
      <li>
        <svg viewBox="0 0 24 24" aria-hidden="true"><rect x="5" y="2" width="14" height="6" rx="1"/><rect x="2" y="9" width="20" height="10" rx="2"/><rect x="6" y="15" width="12" height="7" fill="#fff" stroke="#4a4a4a" stroke-width="1.5"/></svg>
        6482 7315
      </li>
      <li>
        <svg viewBox="0 0 24 24" aria-hidden="true"><path d="M6.6 10.8a15 15 0 0 0 6.6 6.6l2.2-2.2a1 1 0 0 1 1-.25 11.4 11.4 0 0 0 3.6.57 1 1 0 0 1 1 1V20a1 1 0 0 1-1 1A17 17 0 0 1 3 4a1 1 0 0 1 1-1h3.5a1 1 0 0 1 1 1c0 1.25.2 2.45.57 3.57a1 1 0 0 1-.25 1z"/></svg>
        0427 516 903
      </li>
      <li>
        <svg viewBox="0 0 24 24" aria-hidden="true"><path d="M2 5h20v14H2z"/><path d="M2 5l10 8 10-8" fill="none" stroke="#fff" stroke-width="1.6"/></svg>
        marcus.k.wellfare@quorvamail.com
      </li>
      <li>
        <svg viewBox="0 0 24 24" aria-hidden="true"><path d="M10 14a4.5 4.5 0 0 0 6.4 0l3.3-3.3a4.5 4.5 0 0 0-6.4-6.4l-1.4 1.4" fill="none" stroke="#4a4a4a" stroke-width="2.4" stroke-linecap="round"/><path d="M14 10a4.5 4.5 0 0 0-6.4 0l-3.3 3.3a4.5 4.5 0 0 0 6.4 6.4l1.4-1.4" fill="none" stroke="#4a4a4a" stroke-width="2.4" stroke-linecap="round"/></svg>
        www.brindlecovenutrition.com.au
      </li>
    </ul>

    <div class="brand">
      <span class="brand-dot" aria-hidden="true"></span>
      <p class="brand-name">Brindle Cove<br>Nutrition &amp; Dietetics</p>
    </div>

    <div class="band"></div>

    <div class="credential">
      <p class="credential-text">Registered<br>Clinical<br>Nutritionist</p>
      <span class="credential-badge" aria-hidden="true"></span>
    </div>
  </section>

  <section class="card card-back">
    <h2 class="appointment-title">Appointment</h2>
    <ul class="appointment-fields">
      <li><span class="label">Date</span><span class="line"></span></li>
      <li><span class="label">Time</span><span class="line"></span></li>
      <li><span class="label">Location</span><span class="line"></span></li>
    </ul>
  </section>
</body>
</html>
```